Logo + Label Design (Men’s Grooming Brand & Product Packaging)

Design a logo and 2 oz pomade label for Brant, a modern men’s grooming brand focused on clean, high-quality, natural ingredients. The design should establish a bold, masculine, minimalist identity that can later extend to products like shaving gel and body wash.

Key Requirements

Create a primary logo for “Brant” and a core label for the 2 oz pomade jar (screw-top).

Use a clean, modern style — masculine, confident, and approachable (think Wendel’s, Valto, Northfield Mill).

Design for 1–2 color screen printing on solid jar colors (white, black, or navy).

Avoid gradients, foil, or embossing. Must work in black & white.

Provide: vector logo, mockup of the 2 oz jar, color palette (CMYK/RGB/HEX), and font specs.

Winning design may lead to future projects (body wash, shave gel, skincare lines).

Font styles to use
Other font styles liked:
• We like the fonts and design concept in the attached mockup.

Requirements
Should not have
• We want to avoid too much writing or busy designs. We want to avoid having graphics/illustrations embedded in the logo if they will cause the brand to look less classy or sophisticated. We also want the design to look simple and all-American (e.g. Pellham and Stroud, Tall Pine, The BRIM, etc). We’d like to give a Kessler & Dunmore vibe that feels classy and high end.

```html
<!DOCTYPE html>
<html lang="en">
<head>
<meta charset="utf-8">
<title>Brant — Grooming Labels</title>
<link href="https://fonts.googleapis.com/css2?family=Montserrat:wght@500;600;700;800&family=Signika:wght@500;600&display=swap" rel="stylesheet">
<style>
  :root{
    --page:#ffffff;
    --label:#2a2a2c;
    --label-edge:#1f1f21;
    --ink:#ffffff;
    --ink-soft:#d9d9d9;
    --pomade-blue:#38b4ea;
    --shave-teal:#1a9a9c;
    --lotion-magenta:#b23ccb;
    --ring:#4a3f3c;
  }
  *{margin:0;padding:0;box-sizing:border-box}
  html,body{width:1200px;height:784px;overflow:hidden;background:var(--page)}
  .canvas{position:relative;width:1200px;height:784px;font-family:"Montserrat",sans-serif;color:var(--ink)}

  .wordmark{font-family:"Montserrat",sans-serif;font-weight:800;letter-spacing:-0.02em;text-transform:lowercase;color:var(--ink);line-height:1}
  .product-name{font-family:"Montserrat",sans-serif;font-weight:700;letter-spacing:0.06em;line-height:1.05;text-align:center}
  .tagline{font-family:"Signika",sans-serif;font-weight:600;letter-spacing:0.03em;text-transform:uppercase}
  .spec{font-family:"Montserrat",sans-serif;font-weight:500;font-size:8px;letter-spacing:0.02em;line-height:1.35;text-transform:uppercase;text-align:center;color:var(--ink-soft)}
  .divider{width:1px;background:var(--ink)}

  /* lid label */
  .lid{position:absolute;left:40px;top:130px;width:380px;height:380px}
  .lid text{fill:var(--ink)}

  /* tube label */
  .tube{position:absolute;left:470px;top:80px;width:240px;height:480px;background:var(--label);border-radius:4px;display:flex;flex-direction:column;align-items:center;padding-top:56px}
  .tube .wordmark{font-size:38px}
  .tube .accent-icon{margin-top:34px}
  .tube .product-name{font-size:34px;margin-top:30px;letter-spacing:0.1em}
  .tube .tagline{color:var(--shave-teal);font-size:15px;margin-top:34px}
  .tube .spec.formula{margin-top:38px}
  .tube .rule{width:80px;height:1px;background:var(--ink-soft);margin:12px 0}

  /* bottle label */
  .bottle{position:absolute;left:770px;top:130px;width:330px;height:430px;background:var(--label);border-radius:4px;display:flex;flex-direction:column;align-items:center;padding-top:64px}
  .bottle .wordmark{font-size:40px}
  .bottle .accent-icon{margin-top:36px}
  .bottle .product-name{font-size:30px;margin-top:32px}
  .bottle .tagline{color:var(--lotion-magenta);font-size:16px;margin-top:38px}
  .spec-row{display:flex;align-items:center;gap:16px;margin-top:40px}
  .spec-row .divider{height:26px}

  /* jar side band */
  .band{position:absolute;left:300px;top:600px;width:600px;height:130px;background:var(--label);border-radius:4px;display:flex;align-items:center;padding:0 40px}
  .band .wordmark{font-size:46px;margin-right:auto}
  .band-copy{display:flex;flex-direction:column;align-items:center}
  .band .product-name{font-size:26px;letter-spacing:0.08em}
  .band .tagline{color:var(--pomade-blue);font-size:15px;margin-top:8px}
  .band .spec-row{margin-top:10px;gap:14px}
  .band .spec{letter-spacing:0.14em}
  .band .spec-row .divider{height:22px}
</style>
</head>
<body>
<main class="canvas">

  <!-- Pomade lid -->
  <svg class="lid" viewBox="0 0 380 380" aria-label="Hair pomade lid label">
    <defs>
      <path id="lid-arc-top" d="M 30 190 A 160 160 0 0 1 350 190"/>
      <path id="lid-arc-bottom" d="M 38 190 A 152 152 0 0 0 342 190"/>
    </defs>
    <circle cx="190" cy="190" r="188" fill="var(--label-edge)"/>
    <circle cx="190" cy="190" r="178" fill="var(--label)"/>
    <circle cx="190" cy="190" r="170" fill="none" stroke="var(--ring)" stroke-width="0.8"/>
    <text font-family="Montserrat, sans-serif" font-size="7" font-weight="500" letter-spacing="2.2">
      <textPath href="#lid-arc-top" startOffset="50%" text-anchor="middle">FORMULATED TO MINIMIZE SCALP IRRITATION</textPath>
    </text>
    <text font-family="Montserrat, sans-serif" font-size="7" font-weight="500" letter-spacing="2.2">
      <textPath href="#lid-arc-bottom" startOffset="50%" text-anchor="middle">NATURALLY DERIVED PLANT | BEE-BASED INGREDIENTS</textPath>
    </text>
    <text x="190" y="100" text-anchor="middle" font-family="Montserrat, sans-serif" font-weight="800" font-size="34" letter-spacing="-0.5">brant</text>
    <g transform="translate(190 138)">
      <circle r="10" fill="var(--pomade-blue)"/>
      <path d="M0 -7 Q1.2 -1.2 7 0 Q1.2 1.2 0 7 Q-1.2 1.2 -7 0 Q-1.2 -1.2 0 -7Z" fill="var(--label)"/>
    </g>
    <text x="190" y="194" text-anchor="middle" font-family="Montserrat, sans-serif" font-weight="700" font-size="30" letter-spacing="2">HAIR POMADE</text>
    <text x="190" y="232" text-anchor="middle" font-family="Signika, sans-serif" font-weight="600" font-size="16" letter-spacing="0.6" style="fill:var(--pomade-blue)">FRESH &amp; CLEAN</text>
    <text x="140" y="272" text-anchor="middle" font-family="Montserrat, sans-serif" font-weight="500" font-size="7.5">3.4 FL OZ / 100 ML</text>
    <text x="140" y="282" text-anchor="middle" font-family="Montserrat, sans-serif" font-weight="500" font-size="7.5">NET WT.</text>
    <line x1="190" y1="264" x2="190" y2="288" stroke="var(--ink)" stroke-width="1"/>
    <text x="240" y="272" text-anchor="middle" font-family="Montserrat, sans-serif" font-weight="500" font-size="7.5">MEDIUM HOLD</text>
    <text x="240" y="282" text-anchor="middle" font-family="Montserrat, sans-serif" font-weight="500" font-size="7.5">MATTE FINISH</text>
  </svg>

  <!-- Shave gel tube -->
  <section class="tube" aria-label="Shave gel tube label">
    <div class="wordmark">brant</div>
    <svg class="accent-icon" width="20" height="20" viewBox="-10 -10 20 20" aria-hidden="true">
      <circle r="10" fill="var(--shave-teal)"/>
      <path d="M0 -7 Q1.2 -1.2 7 0 Q1.2 1.2 0 7 Q-1.2 1.2 -7 0 Q-1.2 -1.2 0 -7Z" fill="var(--label)"/>
    </svg>
    <h2 class="product-name">SHAVE<br>GEL</h2>
    <p class="tagline">Smooth &amp; Cooling</p>
    <p class="spec formula">Aloe-infused<br>transparent formula</p>
    <div class="rule"></div>
    <p class="spec">3.4 FL OZ / 100 ML<br>Net wt.</p>
  </section>

  <!-- After shave bottle -->
  <section class="bottle" aria-label="After shave lotion bottle label">
    <div class="wordmark">brant</div>
    <svg class="accent-icon" width="20" height="20" viewBox="-10 -10 20 20" aria-hidden="true">
      <circle r="10" fill="var(--lotion-magenta)"/>
      <path d="M0 -7 Q1.2 -1.2 7 0 Q1.2 1.2 0 7 Q-1.2 1.2 -7 0 Q-1.2 -1.2 0 -7Z" fill="var(--label)"/>
    </svg>
    <h2 class="product-name">AFTER SHAVE<br>LOTION</h2>
    <p class="tagline">Calm &amp; Revitalize</p>
    <div class="spec-row">
      <p class="spec">3.4 FL OZ / 100 ML<br>Net wt.</p>
      <span class="divider"></span>
      <p class="spec">Soothing finish<br>Light hydration</p>
    </div>
  </section>

  <!-- Pomade jar side band -->
  <section class="band" aria-label="Hair pomade jar side label">
    <div class="wordmark">brant</div>
    <div class="band-copy">
      <h2 class="product-name">HAIR POMADE</h2>
      <p class="tagline">Fresh &amp; Clean</p>
      <div class="spec-row">
        <span class="divider"></span>
        <p class="spec">Medium hold<br>Matte finish</p>
        <span class="divider"></span>
        <p class="spec">3.4 FL OZ / 100 ML<br>Net wt.</p>
        <span class="divider"></span>
      </div>
    </div>
  </section>

</main>
</body>
</html>
```